SUMMIT GATHERING 2021. August 20th -22nd.

The Hosts of the conference: Grace Tabernacle-Pastors Ron n Della ( Picture with two persons)

Guest Minister: Bishop Lucinda Okotieno. (Cedar Ridge Awakening)

Venue:
Sealand Gateway Lodgeview. 4817 North 239th Avenue Seattle, WA 98174.

Conference times.
Friday August 20th 6pm-8:30pm
Saturday August 21st. 6pm-8:30pm

Sunday August 22nd 10am-1pm
“ CHURCH RENEWAL GATHERING”

5pm-7:30pm
TWOFOLD SURGE GATHERING.

Target Market(s)

18-55

Industry/Entity Type

Religious/ Entertainment.

Requirements
Must have
• A highlight of the Relaunch service on Sunday August 22nd 5pm-7:30pm.
Nice to have
• Excellent ideas….

```html
<!DOCTYPE html>
<html lang="en">
<head>
<meta charset="utf-8">
<title>Summit Gathering 2021 – Grace Tabernacle</title>
<link rel="stylesheet" href="https://fonts.googleapis.com/css2?family=EB+Garamond:wght@500;600;700&family=Teko:wght@500;600&display=swap">
<style>
  :root {
    --stage: #e9e7e3;
    --ink: #1b1b1b;
    --gold: #f0a824;
    --gold-deep: #e29a12;
    --gold-muted: #d9b04a;
    --white: #ffffff;
  }
  * { margin: 0; padding: 0; box-sizing: border-box; }
  html, body { width: 1200px; height: 857px; overflow: hidden; background: var(--stage); }
  .canvas { position: relative; width: 1200px; height: 857px; }
  .poster {
    position: absolute; left: 315px; top: 21px; width: 570px; height: 815px;
    background: var(--ink); overflow: hidden;
    font-family: "EB Garamond", Georgia, serif; color: var(--white);
  }
  .poster-backdrop {
    position: absolute; left: 0; top: 180px; width: 570px; height: 600px;
    background: radial-gradient(ellipse at 45% 55%, #2c2c2c 0%, #1f1f1f 55%, var(--ink) 100%);
  }
  .header-shape { position: absolute; left: 0; top: 0; width: 570px; height: 240px; }
  .brand {
    position: absolute; left: 0; width: 570px; top: 58px; text-align: center;
    font-weight: 700; font-size: 26px; color: var(--ink); letter-spacing: 1px;
  }
  .hosts-portrait { position: absolute; left: 137px; top: 148px; width: 292px; height: 292px; }
  .hosts {
    position: absolute; left: 0; width: 570px; top: 455px; text-align: center;
    color: var(--gold); font-weight: 600; font-size: 34px; letter-spacing: 0.5px; white-space: nowrap;
  }
  .guest-label {
    position: absolute; left: 0; width: 570px; top: 500px; text-align: center;
    font-weight: 500; font-size: 22px; letter-spacing: 2.5px;
  }
  .guest-name {
    position: absolute; left: 0; width: 570px; top: 523px; text-align: center;
    color: var(--gold); font-weight: 600; font-size: 33px; letter-spacing: 0.3px; white-space: nowrap;
  }
  .rule { position: absolute; left: 19px; width: 527px; height: 1px; background: var(--gold-deep); }
  .rule-top { top: 570px; }
  .rule-bottom { top: 646px; }
  .times-tag {
    position: absolute; left: 19px; top: 586px; width: 230px; height: 45px;
    background: var(--gold); color: var(--ink);
    font-family: "Teko", "Arial Narrow", sans-serif; font-weight: 600;
    font-size: 29px; line-height: 50px; text-align: center; letter-spacing: 0.8px;
    white-space: nowrap; overflow: hidden;
  }
  .times-list {
    position: absolute; left: 262px; top: 588px; font-size: 15.5px; font-weight: 600;
    line-height: 23px; list-style: none; white-space: nowrap;
  }
  .times-list .hours { color: var(--gold); }
  .service { position: absolute; top: 665px; width: 276px; text-align: center; }
  .service-left { left: 10px; }
  .service-right { left: 290px; }
  .service-title {
    font-family: "Teko", "Arial Narrow", sans-serif; font-weight: 500;
    color: var(--gold); font-size: 22px; letter-spacing: 1px; line-height: 30px; white-space: nowrap;
  }
  .service-day { font-size: 16px; font-weight: 600; letter-spacing: 0.5px; margin-top: 4px; }
  .service-hours { font-size: 16px; font-weight: 600; color: var(--gold); margin-top: 3px; }
  .service-divider { position: absolute; left: 295px; top: 664px; width: 1px; height: 92px; background: var(--gold-deep); }
  .venue {
    position: absolute; left: 9px; top: 781px; width: 548px; height: 28px;
    background: var(--gold-muted); color: var(--ink);
    font-size: 11.6px; font-weight: 500; line-height: 29px; text-align: center; letter-spacing: 0.1px; white-space: nowrap;
  }
</style>
</head>
<body>
<main class="canvas">
  <article class="poster">
    <div class="poster-backdrop" role="img" aria-label="Faint dark photograph of a church building behind the text"></div>

    <svg class="header-shape" viewBox="0 0 570 240" aria-hidden="true">
      <path d="M0,0 H570 V110 C520,200 420,234 285,234 C150,234 50,200 0,110 Z" fill="var(--gold)"/>
      <path d="M0,0 H570 V30 C560,150 430,218 285,218 C140,218 10,150 0,30 Z" fill="var(--white)"/>
    </svg>

    <div class="brand">Grace Tabernacle</div>

    <svg class="hosts-portrait" viewBox="0 0 292 292" role="img" aria-label="Photograph of the host pastors, a smiling couple">
      <defs>
        <linearGradient id="portraitTone" x1="0" y1="0" x2="1" y2="1">
          <stop offset="0" stop-color="#4a3a48"/>
          <stop offset="0.55" stop-color="#8a3fb0"/>
          <stop offset="1" stop-color="#c24fa3"/>
        </linearGradient>
      </defs>
      <circle cx="146" cy="146" r="144" fill="none" stroke="var(--gold)" stroke-width="2"/>
      <circle cx="146" cy="146" r="133" fill="url(#portraitTone)" stroke="var(--gold)" stroke-width="2"/>
    </svg>

    <h1 class="hosts">PASTORS RON N DELLA</h1>
    <p class="guest-label">GUEST MINISTER:</p>
    <h2 class="guest-name">BISHOP LUCINDA OKOTIENO</h2>

    <div class="rule rule-top"></div>
    <div class="times-tag">CONFERENCE TIMES</div>
    <ul class="times-list">
      <li>FRIDAY 20TH AUGUST | <span class="hours">6PM-8:30PM</span></li>
      <li>SATURDAY 21ST AUGUST | <span class="hours">6PM-8:30PM</span></li>
    </ul>
    <div class="rule rule-bottom"></div>

    <section class="service service-left">
      <h3 class="service-title">CHURCH RENEWAL GATHERING</h3>
      <p class="service-day">SUNDAY 22ND AUGUST</p>
      <p class="service-hours">10AM-1PM</p>
    </section>
    <div class="service-divider"></div>
    <section class="service service-right">
      <h3 class="service-title">TWOFOLD SURGE GATHERING</h3>
      <p class="service-day">SUNDAY 22ND AUGUST</p>
      <p class="service-hours">5PM-7:30PM</p>
    </section>

    <p class="venue">VENUE: SEALAND GATEWAY LODGEVIEW. 4817 NORTH 239TH AVENUE SEATTLE, WA 98174.</p>
  </article>
</main>
</body>
</html>
```